Les Aliments Corvasi 2 sided flyer

We have a restaurant in St.Leonard, Montreal east, called Restaurant Corvasi and now we are bringing our product (food) to the South Shore of Montreal in Brossard as Les Aliments Corvasi not as a restaurant but as a frozen food store.

- We are a frozen store. (not a restaurant just a reminder) (almost like a grocery store)
- Selling homemade Italian food prepared in location, frozen and vacuumed packed.

- I need flyers telling the public that we are Bringing Corvasi's (frozen food) to the South Shore with my logo, few picture, and my location.

Industry/Entity Type

Food Production

Font styles to use
Sans Serif

Colors
ffffff
000000

Requirements
Must have
• address: 4710 Boul. Marchetière
• Brossard, Quebec
• J3R 2K9
• our email address : alimentscorvasi@courrielbleu.ca
• -flyer must be in french, i can supply the translation if needed
• needs to be refreshing, appealing, and attract the public
Nice to have
• the color burgundy is not available would like to see how it looks with that color to match my sign and logo
• the flyer has to be in french because I live in Quebec and its the law here
Should not have
• should not hurt the eyes when reading

```html
<!DOCTYPE html>
<html lang="en">
<head>
<meta charset="utf-8">
<title>Les Aliments Corvasi – Flyer</title>
<link rel="stylesheet" href="https://fonts.googleapis.com/css2?family=Lato:ital,wght@0,400;0,700;0,900;1,400&family=Oswald:wght@500;700&family=Great+Vibes&display=swap">
<style>
  :root {
    --page: #ffffff;
    --ink: #000000;
    --charcoal: #141414;
    --wood-dark: #1d1d1d;
    --burgundy: #b3172a;
    --bright-red: #e0192c;
    --paper: #f3f3f3;
    --paper-shade: #d9d9d9;
    --text-grey: #222222;
  }
  * { box-sizing: border-box; margin: 0; padding: 0; }
  html, body { width: 1200px; height: 900px; overflow: hidden; background: var(--page); }
  .canvas { position: relative; width: 1200px; height: 900px; background: var(--page); font-family: "Lato", sans-serif; }

  .flyer { position: absolute; top: 108px; width: 466px; height: 660px; overflow: hidden; box-shadow: 0 2px 8px rgba(0,0,0,.25); }
  .flyer--front { left: 100px; background: linear-gradient(90deg, #111 0%, var(--wood-dark) 30%, #0e0e0e 55%, #222 80%, #121212 100%); color: #fff; }
  .flyer--back { left: 633px; background: linear-gradient(180deg, var(--paper) 0%, #ececec 45%, var(--paper-shade) 100%); color: var(--ink); }

  .frame { position: absolute; border: 1px solid; }
  .flyer--front .frame { left: 30px; top: 24px; width: 406px; height: 614px; border-color: rgba(255,255,255,.85); }
  .flyer--back .frame { left: 30px; top: 23px; width: 408px; height: 612px; border-color: var(--ink); }

  .brand { position: absolute; left: 0; width: 100%; text-align: center; }
  .brand__name { display: inline-flex; align-items: center; gap: 10px; font-family: "Oswald", sans-serif; font-weight: 500; font-size: 30px; letter-spacing: 1px; line-height: 1; }
  .brand__dot { width: 14px; height: 14px; border-radius: 50%; display: inline-block; }
  .flyer--front .brand { top: 98px; }
  .flyer--front .brand__name { color: #fff; }
  .flyer--front .brand__dot { background: #fff; }
  .flyer--back .brand { top: 110px; }
  .flyer--back .brand__name { color: var(--burgundy); font-size: 32px; }
  .flyer--back .brand__dot { background: var(--burgundy); }

  .front__intro { position: absolute; left: 50px; width: 366px; top: 159px; text-align: center; font-style: italic; font-size: 10.5px; line-height: 16px; color: #eee; }
  .front__rule { position: absolute; left: 150px; width: 166px; top: 197px; height: 1px; background: rgba(255,255,255,.35); }
  .front__phone { position: absolute; left: 0; width: 100%; top: 204px; text-align: center; font-size: 35px; font-weight: 700; color: var(--bright-red); letter-spacing: 0.5px; }
  .front__address { position: absolute; left: 0; width: 100%; top: 243px; text-align: center; font-style: italic; font-size: 11.5px; color: #eee; }

  .front__photo { position: absolute; left: 0; top: 330px; width: 466px; height: 330px;
    background: radial-gradient(ellipse at 35% 70%, #e4501b 0%, #c9341a 30%, rgba(150,30,20,.7) 55%, rgba(20,20,20,0) 80%); }

  .badge { position: absolute; left: 235px; top: 310px; width: 165px; height: 165px; }
  .badge__text { position: absolute; left: 245px; top: 333px; width: 140px; text-align: center; font-family: "Great Vibes", cursive; font-size: 27px; line-height: 34px; color: #fff; }

  .dishes { position: absolute; top: 173px; left: 0; width: 100%; }
  .dish { position: absolute; top: 0; width: 118px; height: 118px; border-radius: 50%; border: 2px solid var(--ink); padding: 4px; background: #fff; }
  .dish__photo { width: 100%; height: 100%; border-radius: 50%; border: 3px solid var(--burgundy); }
  .dish--one { left: 48px; } .dish--one .dish__photo { background: radial-gradient(circle at 50% 60%, #d9a95a, #b7823a 60%, #8a5a2a); }
  .dish--two { left: 176px; } .dish--two .dish__photo { background: radial-gradient(circle at 50% 65%, #e05a25, #b83a1c 55%, #6f7a6a); }
  .dish--three { left: 303px; } .dish--three .dish__photo { background: radial-gradient(circle at 50% 50%, #f0b74a, #dc8e2e 60%, #9e5a22); }

  .back__kicker { position: absolute; left: 0; width: 100%; top: 319px; text-align: center; font-family: "Lato", sans-serif; font-weight: 900; font-size: 9.5px; letter-spacing: .4px; }
  .back__headline { position: absolute; left: 0; width: 100%; top: 330px; text-align: center; font-family: "Oswald", sans-serif; font-weight: 700; font-size: 25px; letter-spacing: .3px; }

  .info { position: absolute; top: 383px; }
  .info--left { left: 55px; width: 195px; }
  .info--right { left: 280px; width: 153px; }
  .info__label { display: block; height: 21px; line-height: 21px; text-align: center; background: var(--burgundy); color: #fff; font-weight: 700; font-size: 11px; width: 135px; }
  .info--left .info__label { margin-left: 13px; }
  .info__body { margin-top: 17px; font-size: 7.3px; line-height: 9.6px; color: var(--text-grey); }
  .info__body p { margin-bottom: 9.6px; }
  .info--right .info__body { text-align: justify; }

  .back__call { position: absolute; left: 55px; top: 545px; font-weight: 900; font-size: 12px; letter-spacing: .3px; }
  .back__phone { position: absolute; left: 51px; top: 560px; font-weight: 700; font-size: 26px; color: var(--burgundy); letter-spacing: .5px; }
  .back__address { position: absolute; left: 55px; top: 592px; font-style: italic; font-size: 8px; color: var(--text-grey); }
  .back__email { position: absolute; left: 280px; top: 565px; width: 140px; height: 19px; line-height: 19px; background: var(--burgundy); color: #fff; font-style: italic; font-size: 8px; text-align: center; }
</style>
</head>
<body>
<main class="canvas">

  <section class="flyer flyer--front">
    <div class="front__photo" role="img" aria-label="Photo of two glass jars of tomato sauce topped with basil leaves, with fresh tomatoes"></div>
    <div class="frame"></div>
    <div class="brand"><span class="brand__name"><span class="brand__dot"></span>LES ALIMENTS CORVASI</span></div>
    <p class="front__intro">we are bringing our product (food) to the South Shore of Montreal in Brossard as Les Aliments Corvasi not as a restaurant but as a frozen food store</p>
    <div class="front__rule"></div>
    <p class="front__phone">450.555.0171</p>
    <p class="front__address">4710 Boul. Marchetière ,Brossard, Quebec,J3R 2K9</p>
    <svg class="badge" viewBox="0 0 165 165" aria-hidden="true">
      <circle cx="82.5" cy="82.5" r="78" fill="none" stroke="#ffffff" stroke-width="2"/>
      <path d="M 160 70 A 78 78 0 0 1 60 157" fill="none" stroke="#b3172a" stroke-width="3"/>
    </svg>
    <p class="badge__text">We are a<br>frozen<br>store</p>
  </section>

  <section class="flyer flyer--back">
    <div class="frame"></div>
    <div class="brand"><span class="brand__name"><span class="brand__dot"></span>LES ALIMENTS CORVASI</span></div>

    <div class="dishes">
      <div class="dish dish--one"><div class="dish__photo" role="img" aria-label="Photo of a baked lasagna dish"></div></div>
      <div class="dish dish--two"><div class="dish__photo" role="img" aria-label="Photo of a jar of tomato sauce with basil"></div></div>
      <div class="dish dish--three"><div class="dish__photo" role="img" aria-label="Photo of a cheese pizza"></div></div>
    </div>

    <p class="back__kicker">WE SELLING HOMEMADE ITALIAN FOOD PREPARED IN LOCATION</p>
    <h1 class="back__headline">FROZEN AND VACUUMED PACKED</h1>

    <div class="info info--left">
      <span class="info__label">What is Lorem Ipsum</span>
      <div class="info__body">
        <p>Lorem ipsum dolor sit amet, consectetur adipiscing elit.</p>
        <p>Fusce in mauris et mi vulputate volutpat.<br>Integer aliquam ante id eros pulvinar, et ornare dolor aliquam.</p>
        <p>Proin eget libero sit amet lectus hendrerit fringilla non vitae ex.</p>
        <p>Proin finibus est rhoncus pharetra tristique.</p>
      </div>
    </div>

    <div class="info info--right">
      <span class="info__label">What is Lorem Ipsum</span>
      <div class="info__body">
        <p>Lorem Ipsum is simply dummy text of the printing and typesetting industry. Lorem Ipsum has been the industry's standard dummy text ever since the 1500s, when an unknown printer took a galley of type and scrambled it to make a type specimen book.</p>
        <p>Lorem Ipsum is simply dummy text of the printing and typesetting industry. Lorem Ipsum has been the industry's standard dummy text ever since the 1500s, when an unknown printer took a galley of type and scrambled it to make a type specimen book.</p>
      </div>
    </div>

    <p class="back__call">FOR MORE DETAIL CALL US</p>
    <p class="back__phone">450.555.0171</p>
    <p class="back__address">4710 Boul. Marchetière ,Brossard, Quebec,J3R 2K9</p>
    <p class="back__email">alimentscorvasi@courrielbleu.ca</p>
  </section>

</main>
</body>
</html>
```